Company growth chart/Vision for the next 10 years of growth

I need to show an illustration how the company will grow over the next 10 years. Develop graphic to communicate:

In the center / or main focus ar...

Target Market(s)

Employees in corporate / need to show a future vision to get everyone excited about. Not a growth "tree".

Industry/Entity Type

It Company

Requirements
Must have
• Be an illustration/graphic showing what the project description states.
Nice to have
• I've looked at gears/mountains/icons to showcase this vision and I haven't been able to come up with anything.
Should not have
• A growth tree. Not what I'm looking for. This is corporate.

```html
<!DOCTYPE html>
<html lang="en">
<head>
<meta charset="utf-8">
<title>Vision – 10 Year Target</title>
<link href="https://fonts.googleapis.com/css2?family=Montserrat:wght@500;600;700;800&family=Oswald:wght@600;700&display=swap" rel="stylesheet">
<style>
  :root{
    --blue:#1f6fb8;
    --orange:#f7941d;
    --red-orange:#ff3d00;
    --magenta:#b5076f;
    --teal:#00b5c4;
    --purple:#2e0a4f;
    --ink:#3a3a3a;
    --white:#ffffff;
    --stripe:#cfd6e2;
  }
  *{margin:0;padding:0;box-sizing:border-box}
  html,body{width:927px;height:1200px;overflow:hidden;background:var(--white)}
  body{position:relative;font-family:"Montserrat",sans-serif;color:var(--ink)}
  .abs{position:absolute}
  .header{left:0;top:0;width:927px;height:163px;background:var(--blue)}
  .title{left:60px;top:30px;font-weight:800;font-size:108px;letter-spacing:1px;color:var(--white);line-height:1;white-space:nowrap}
  .target{left:482px;top:34px;font-size:36px;font-weight:500;color:var(--white);line-height:48px;letter-spacing:1px;white-space:nowrap}
  .target b{color:var(--orange);font-weight:800}
  .stripes{left:0;width:927px;height:26px;background:repeating-linear-gradient(90deg,var(--stripe) 0 2px,transparent 2px 4px)}
  .stripes.top{top:164px;opacity:.7}
  .stripes.bottom{top:1173px;background:repeating-linear-gradient(90deg,var(--blue) 0 2px,transparent 2px 4px);opacity:.8}
  .stat-label{font-size:17px;font-weight:600;line-height:1.3;color:var(--ink);white-space:nowrap}
  .stat-num{font-family:"Oswald",sans-serif;font-weight:700;color:var(--blue);line-height:1;letter-spacing:-1px;white-space:nowrap;transform-origin:left top}
  .stat-num.narrow{transform:scaleX(.62)}
  .divider{width:2px;background:#444}
  .box-title{font-weight:800;font-size:30px;line-height:1.25;color:var(--ink);white-space:nowrap}
  .box-list{font-size:17px;font-weight:600;line-height:1.3;color:var(--ink);white-space:nowrap}
  .badge{width:42px;height:42px;border-radius:10px;background:var(--white);border:3px solid;display:flex;align-items:center;justify-content:center;font-weight:800;font-size:32px;color:#222}
  .placeholder{border-radius:8px}
  .count{width:36px;height:36px;border-radius:50%;color:var(--white);font-weight:700;font-size:17px;display:flex;align-items:center;justify-content:center}
</style>
</head>
<body>
  <div class="abs header"></div>
  <div class="abs title">VISION</div>
  <div class="abs target"><b>10 YEAR</b> TARGET<br>FUTURE DATE: <b>2026</b></div>
  <div class="abs stripes top"></div>

  <!-- stats row one -->
  <svg class="abs" style="left:28px;top:214px" width="78" height="80" viewBox="0 0 78 80" aria-hidden="true">
    <rect x="2" y="2" width="74" height="76" fill="none" stroke="#444" stroke-width="4"/>
    <g fill="none" stroke="#444" stroke-width="3">
      <rect x="11" y="12" width="14" height="12"/><rect x="32" y="12" width="14" height="12"/><rect x="53" y="12" width="14" height="12"/>
      <rect x="11" y="33" width="14" height="12"/><rect x="32" y="33" width="14" height="12"/><rect x="53" y="33" width="14" height="12"/>
      <rect x="11" y="54" width="14" height="18"/><rect x="32" y="54" width="14" height="22"/><rect x="53" y="54" width="14" height="18"/>
    </g>
  </svg>
  <div class="abs stat-label" style="left:121px;top:212px">Building Square<br>Footage Impact:</div>
  <div class="abs stat-num" style="left:122px;top:260px;font-size:33px">500,000 SF</div>
  <div class="abs divider" style="left:286px;top:216px;height:78px"></div>

  <svg class="abs" style="left:300px;top:214px" width="72" height="80" viewBox="0 0 74 84" aria-hidden="true">
    <g fill="none" stroke="#444" stroke-width="2.5">
      <circle cx="18" cy="10" r="7"/><circle cx="36" cy="14" r="7"/><circle cx="56" cy="14" r="7"/>
      <path d="M6 82V28h24v54M14 50v32M22 50v32"/>
      <path d="M26 82V32h22v50M33 52v30M41 52v30"/>
      <path d="M46 82V32h22v50M53 52v30M61 52v30"/>
    </g>
  </svg>
  <div class="abs stat-label" style="left:383px;top:233px">Employee<br>engagement<br>rating of</div>
  <div class="abs stat-num narrow" style="left:506px;top:224px;font-size:72px">90%</div>
  <div class="abs divider" style="left:600px;top:226px;height:68px"></div>

  <svg class="abs" style="left:614px;top:214px" width="82" height="82" viewBox="0 0 82 84" aria-hidden="true">
    <g fill="none" stroke="#444" stroke-width="2.5" stroke-linejoin="round">
      <path d="M14 8l3 7 7 .5-5.5 4.5 2 7-6.5-4-6.5 4 2-7L4 15.5l7-.5z"/>
      <path d="M41 2l3 7 7 .5-5.5 4.5 2 7-6.5-4-6.5 4 2-7L31 9.5l7-.5z"/>
      <path d="M68 8l3 7 7 .5-5.5 4.5 2 7-6.5-4-6.5 4 2-7L58 15.5l7-.5z"/>
      <circle cx="40" cy="54" r="24"/><circle cx="40" cy="47" r="8"/>
      <path d="M25 70c3-9 9-12 15-12s12 3 15 12"/>
      <circle cx="64" cy="70" r="12" fill="#fff"/><path d="M58 70l4 4 8-8"/>
    </g>
  </svg>
  <div class="abs stat-label" style="left:707px;top:234px">Customer<br>satisfaction<br>rating of</div>
  <div class="abs stat-num narrow" style="left:818px;top:226px;font-size:72px">95%</div>

  <!-- stats row two -->
  <svg class="abs" style="left:166px;top:316px" width="54" height="58" viewBox="0 0 54 58" aria-hidden="true">
    <path d="M27 3l22 8v18c0 13-9 22-22 27C14 51 5 42 5 29V11z" fill="none" stroke="#444" stroke-width="4" stroke-linejoin="round"/>
    <path d="M16 29l8 8 15-15" fill="none" stroke="#444" stroke-width="4"/>
  </svg>
  <div class="abs stat-label" style="left:226px;top:327px">Safety EMR<br>at or below</div>
  <div class="abs stat-num" style="left:342px;top:314px;font-size:60px">0.65</div>
  <div class="abs divider" style="left:465px;top:317px;height:55px"></div>
  <svg class="abs" style="left:480px;top:312px" width="82" height="56" viewBox="0 0 86 56" aria-hidden="true">
    <g fill="none" stroke="#444" stroke-width="2.2">
      <circle cx="10" cy="12" r="5"/><circle cx="26" cy="8" r="5"/><circle cx="43" cy="6" r="5"/><circle cx="60" cy="8" r="5"/><circle cx="76" cy="12" r="5"/>
      <path d="M3 54V22h14v32M19 54V18h14v36M36 54V16h14v38M53 54V18h14v36M69 54V22h14v32"/>
    </g>
  </svg>
  <div class="abs stat-num" style="left:568px;top:314px;font-size:60px">160</div>
  <div class="abs stat-label" style="left:661px;top:352px">Employees</div>

  <!-- frames and centre -->
  <svg class="abs" style="left:0;top:0" width="927" height="1200" viewBox="0 0 927 1200" aria-hidden="true">
    <defs>
      <radialGradient id="hub" cx="50%" cy="45%" r="55%">
        <stop offset="0" stop-color="#ffffff"/><stop offset=".8" stop-color="#f2f2f2"/><stop offset="1" stop-color="#d6d6d6"/>
      </radialGradient>
    </defs>
    <rect x="96" y="514" width="268" height="366" rx="24" fill="none" stroke="var(--magenta)" stroke-width="3"/>
    <path d="M94 852h350v30H120a26 26 0 0 1-26-26z" fill="var(--magenta)"/>
    <rect x="360" y="409" width="366" height="300" rx="22" fill="#fff" stroke="var(--red-orange)" stroke-width="3"/>
    <path d="M382 408a24 24 0 0 0-24 24v330h28V408z" fill="var(--red-orange)"/>
    <rect x="200" y="862" width="368" height="284" rx="22" fill="#fff" stroke="var(--purple)" stroke-width="3"/>
    <path d="M542 790h28v334a24 24 0 0 1-24 24h-4z" fill="var(--purple)"/>
    <rect x="488" y="672" width="344" height="368" rx="24" fill="#fff" stroke="var(--teal)" stroke-width="3"/>
    <path d="M480 670h328a26 26 0 0 1 26 26v2H480z" fill="var(--teal)"/>
    <circle cx="464" cy="776" r="132" fill="var(--blue)"/>
    <circle cx="464" cy="776" r="106" fill="#fff"/>
    <circle cx="464" cy="776" r="90" fill="url(#hub)"/>
  </svg>

  <div class="abs placeholder" role="img" aria-label="Line icon of a document with an eye and plus sign" style="left:414px;top:724px;width:104px;height:104px;background:linear-gradient(135deg,#dbe8f5,#c3d9ee);border-radius:50%"></div>

  <!-- team growth -->
  <div class="abs badge" style="left:366px;top:424px;border-color:var(--red-orange)">1</div>
  <div class="abs box-title" style="left:423px;top:426px;font-size:28px">Team Growth</div>
  <div class="abs placeholder" role="img" aria-label="Small group of people icons" style="left:404px;top:510px;width:90px;height:70px;background:linear-gradient(#ececec,#dcdcdc)"></div>
  <div class="abs count" style="left:432px;top:569px;background:#333">20</div>
  <svg class="abs" style="left:497px;top:505px" width="36" height="36" viewBox="0 0 36 36" aria-hidden="true"><path d="M2 12h16V2l16 16-16 16V24H2z" fill="var(--orange)"/></svg>
  <div class="abs placeholder" role="img" aria-label="Large group of people icons" style="left:536px;top:478px;width:178px;height:102px;background:linear-gradient(#e3eef8,#cfe0f1)"></div>
  <div class="abs count" style="left:607px;top:569px;background:var(--blue)">100</div>

  <!-- vertical market -->
  <div class="abs box-list" style="left:107px;top:528px">Hotels, Trade Labor<br>Subcontracting, Specialty<br>Retail, Quick Service<br>Restaurants</div>
  <div class="abs placeholder" role="img" aria-label="Line icon of a shop counter with a cashier" style="left:106px;top:640px;width:108px;height:108px;background:linear-gradient(#e3eef8,#cfe0f1)"></div>
  <div class="abs box-title" style="left:107px;top:752px">Vertical<br>Market Focus</div>
  <div class="abs badge" style="left:105px;top:834px;border-color:var(--magenta)">4</div>

  <!-- personal development -->
  <div class="abs badge" style="left:776px;top:686px;border-color:var(--teal)">2</div>
  <div class="abs box-title" style="left:611px;top:700px">Personal<br>Development</div>
  <div class="abs placeholder" role="img" aria-label="Line icon of a gear beside a person" style="left:610px;top:784px;width:106px;height:106px;background:linear-gradient(#e3eef8,#cfe0f1)"></div>

  <!-- regional -->
  <div class="abs box-list" style="left:241px;top:909px">Hotels, Manufacturing,<br>Retail, Office,<br>Sr. Housing,<br>Hospitals</div>
  <div class="abs placeholder" role="img" aria-label="Line icon of city buildings" style="left:376px;top:958px;width:120px;height:100px;background:linear-gradient(#e3eef8,#cfe0f1)"></div>
  <div class="abs box-title" style="left:242px;top:1064px">Current Regional<br>Market Focus</div>
  <div class="abs badge" style="left:518px;top:1088px;border-color:var(--purple)">3</div>

  <div class="abs stripes bottom"></div>
</body>
</html>
```